Bright Meadow Notes Wordpress Blog

I need to design a WordPress blog page. The name of the Blog is "Bright Meadow Notes". I am hoping for a simple design that is easy for me to post future posts to. I like the color teal for this. The website is brightmeadownotes.example where I am going to write a personal blog. I don't have a logo for this, but am hoping for a header that has some swirly, but classy looking text. Easy on the eyes. The website will only have a couple of pages - the home landing page, and an about me page.

Font styles to use
Script

Colors
00a990
86cfc6
cfeae6

Requirements
Must have
• A header for the landing page of the blog. Clean layout of where the blog posts will lie.

```html
<!DOCTYPE html>
<html lang="en">
<head>
<meta charset="utf-8">
<title>Bright Meadow Notes</title>
<link href="https://fonts.googleapis.com/css2?family=Great+Vibes&family=Courgette&family=Open+Sans:wght@400;600;700&display=swap" rel="stylesheet">
<style>
:root{
  --teal:#00a990;
  --teal-mid:#86cfc6;
  --teal-light:#cfeae6;
  --page:#eef0f0;
  --white:#ffffff;
  --ink:#333b3d;
  --muted:#8a9194;
  --line:#dde1e2;
  --footer:#e3e6e7;
}
*{box-sizing:border-box;margin:0;padding:0}
html,body{width:1200px;height:2936px;overflow:hidden}
body{background:var(--page);font-family:"Open Sans",Arial,sans-serif;color:var(--ink);position:relative}
.abs{position:absolute}

/* header */
.site-header{left:0;top:0;width:1200px;height:256px;background:var(--white)}
.header-curve{left:0;top:0;width:1200px;height:70px}
.connect{left:72px;top:128px;font-size:13px;font-weight:700;letter-spacing:.5px}
.social{display:flex;gap:12px;left:72px;top:154px}
.social span{width:16px;height:16px;border-radius:50%;background:#9aa2a5;display:block}
.brand{left:0;width:1200px;top:118px;text-align:center;font-family:"Great Vibes",cursive;font-size:76px;color:var(--teal);line-height:1}
.search{left:944px;top:136px;width:200px;height:40px;border:1px solid var(--line);border-radius:3px;font-size:14px;color:var(--muted);padding:10px 12px}
.search svg{position:absolute;right:10px;top:11px}

/* nav */
.main-nav{left:0;top:256px;width:1200px;height:56px;background:var(--teal);display:flex;justify-content:center;align-items:center;gap:44px}
.main-nav a{color:var(--white);font-size:14px;font-weight:600;text-decoration:none;letter-spacing:.5px}

/* hero */
.hero{left:0;top:312px;width:1200px;height:428px;background:linear-gradient(180deg,#f1d890 0%,#f0b64a 45%,#c77a1e 80%,#6b4a22 100%)}
.hero-title{left:72px;top:420px;font-size:48px;font-weight:700;color:var(--ink)}
.hero-sub{left:72px;top:484px;width:520px;font-size:22px;font-weight:600;color:var(--teal);line-height:1.35}
.dots{left:72px;top:684px;display:flex;gap:10px}
.dots span{width:10px;height:10px;border-radius:50%;background:rgba(255,255,255,.6)}
.dots span:first-child{background:var(--white)}

/* sidebar */
.widget{background:var(--white);left:72px;width:328px;padding:24px}
.widget-title{font-family:"Courgette",cursive;color:var(--teal);font-size:26px;text-align:center;line-height:1.2}
.avatar{width:150px;height:150px;border-radius:50%;margin:20px auto;background:linear-gradient(160deg,#f3d7c6,#d9a88e);border:4px solid var(--teal-light)}
.widget p{font-size:13px;line-height:1.7;color:var(--muted);text-align:center;font-style:italic}
.widget-social{display:flex;justify-content:center;gap:38px;margin-top:34px;padding-top:26px;border-top:1px solid var(--line)}
.widget-social span{width:18px;height:18px;border-radius:50%;background:#9aa2a5;display:block}
.email-input{margin:22px 0 12px;height:38px;border:1px solid var(--line);border-radius:3px;font-size:13px;color:var(--muted);text-align:center;line-height:36px}
.btn-subscribe{height:38px;background:#4a5558;color:var(--white);font-size:13px;font-weight:700;text-align:center;line-height:38px;border-radius:3px;letter-spacing:1px}
.recent{list-style:none;margin-top:18px}
.recent li{display:flex;gap:14px;margin-bottom:22px}
.thumb{width:90px;height:66px;flex:none}
.recent strong{display:block;font-size:13px;font-weight:600;line-height:1.45}
.recent em{font-size:11px;color:var(--muted);font-style:normal}
.archive{list-style:none;margin-top:16px}
.archive li{font-size:14px;color:var(--muted);line-height:2}
.tags{display:flex;flex-wrap:wrap;gap:6px 16px;margin-top:16px;font-size:13px;color:var(--muted)}

/* posts */
.post{position:absolute}
.post-title{font-size:28px;font-weight:600;color:var(--ink);white-space:nowrap}
.post-small .post-title{font-size:25px}
.share{position:absolute;right:0;top:2px;width:30px;height:30px;background:var(--line);border-radius:3px}
.meta{display:flex;gap:28px;font-size:12px;color:var(--muted);margin-top:12px;align-items:center}
.meta span{display:flex;gap:6px;align-items:center}
.post-image{margin-top:14px;width:100%}
.excerpt{font-size:13px;line-height:1.7;color:var(--muted);font-style:italic;margin-top:20px}
.post-foot{display:flex;justify-content:space-between;align-items:center;margin-top:28px;padding-top:14px;border-top:1px solid var(--line);font-size:13px}
.read-more{color:var(--teal);font-weight:600}
.comments{color:var(--muted);display:flex;gap:6px;align-items:center}

.pagination{left:632px;top:2704px;display:flex;gap:8px}
.pagination span{width:34px;height:34px;background:var(--line);color:var(--ink);font-size:14px;display:flex;align-items:center;justify-content:center;border-radius:3px}
.pagination .active,.pagination .arrow{background:var(--teal);color:var(--white)}

.site-footer{left:0;top:2800px;width:1200px;height:136px;background:var(--footer);text-align:center;font-size:13px;color:var(--muted);padding-top:52px}
</style>
</head>
<body>

<header class="site-header abs">
  <svg class="header-curve abs" viewBox="0 0 1200 70" aria-hidden="true">
    <path d="M0 0 H1200 V22 Q900 64 600 40 Q300 64 0 22 Z" fill="var(--page)"/>
    <path d="M0 22 Q300 64 600 40 Q900 64 1200 22" fill="none" stroke="var(--teal-mid)" stroke-width="2"/>
  </svg>
  <div class="connect abs">CONNECT ME</div>
  <div class="social abs"><span></span><span></span><span></span><span></span><span></span></div>
  <div class="brand abs">Bright Meadow Notes</div>
  <div class="search abs">Search...
    <svg width="16" height="16" viewBox="0 0 16 16"><circle cx="6.5" cy="6.5" r="5" fill="none" stroke="#8a9194" stroke-width="2"/><line x1="10.5" y1="10.5" x2="15" y2="15" stroke="#8a9194" stroke-width="2"/></svg>
  </div>
</header>

<nav class="main-nav abs">
  <a href="#">HOME</a><a href="#">ABOUT MAYA</a><a href="#">CONTACT</a>
</nav>

<section class="hero abs" role="img" aria-label="Photo of a woman raising her arms toward a golden sunset"></section>
<div class="hero-title abs">WELCOME TO MY SITE</div>
<div class="hero-sub abs">Vestibulum ante ipsum primis in faucibus orci luctus et ultrices posuere cubilia.</div>
<div class="dots abs"><span></span><span></span><span></span><span></span></div>

<!-- sidebar -->
<aside>
  <div class="widget abs" style="top:792px;height:478px">
    <h3 class="widget-title">About Maya</h3>
    <div class="avatar" role="img" aria-label="Portrait photo of the blog author"></div>
    <p>Aliquam molestie, mi id imperdiet euismod, dui purus auctor tellus, et interdum lacus lectus ac ante.</p>
    <p style="margin-top:10px">Sed accumsan sollicitudin sapien, sit amet adipiscing turpis gravida ac. In congue, neque ac lobortis volutpat, libero mauris cursus mi, vitae suscipit.</p>
    <div class="widget-social"><span></span><span></span><span></span><span></span></div>
  </div>

  <div class="widget abs" style="top:1290px;height:240px">
    <h3 class="widget-title">Get All the New Updates<br>to Your Inbox</h3>
    <div class="email-input">Enter Email Address</div>
    <div class="btn-subscribe">SUBSCRIBE ›</div>
  </div>

  <div class="widget abs" style="top:1550px;height:580px">
    <h3 class="widget-title" style="text-align:left">Recent Posts</h3>
    <ul class="recent">
      <li><div class="thumb" role="img" aria-label="Sunset landscape thumbnail" style="background:linear-gradient(#f2c35a,#b0702a)"></div><div><strong>Lorem ipsum dolor purus aliquam...</strong><em>Mar 16, 2017</em></div></li>
      <li><div class="thumb" role="img" aria-label="Goal chart thumbnail" style="background:linear-gradient(#e9eef2,#9cc4d8)"></div><div><strong>Lorem ipsum dolor purus aliquam...</strong><em>Mar 16, 2017</em></div></li>
      <li><div class="thumb" role="img" aria-label="Person celebrating thumbnail" style="background:linear-gradient(#f2f2f2,#c9c9c9)"></div><div><strong>Lorem ipsum dolor purus aliquam...</strong><em>Mar 16, 2017</em></div></li>
      <li><div class="thumb" role="img" aria-label="Friends at sunset thumbnail" style="background:linear-gradient(#f4a640,#5a3a1c)"></div><div><strong>Lorem ipsum dolor purus aliquam...</strong><em>Mar 16, 2017</em></div></li>
      <li><div class="thumb" role="img" aria-label="Green dial thumbnail" style="background:linear-gradient(#6a8f4a,#1e2b1c)"></div><div><strong>Lorem ipsum dolor purus aliquam...</strong><em>Mar 16, 2017</em></div></li>
    </ul>
  </div>

  <div class="widget abs" style="top:2150px;height:300px">
    <h3 class="widget-title" style="text-align:left">Archive</h3>
    <ul class="archive">
      <li>March 2017</li><li>February 2017</li><li>January 2017</li><li>December 2016</li><li>November 2016</li>
    </ul>
  </div>

  <div class="widget abs" style="top:2500px;height:270px">
    <h3 class="widget-title" style="text-align:left">Tags</h3>
    <div class="tags">
      <span>Aliquam</span><span>Molestie</span><span>Purus auctor</span><span>Tellus</span><span>Interdum</span><span>Lacus</span><span>Sed</span><span>Accumsan</span><span>Sollicitudin</span><span>Adipiscing</span><span>Turpis</span><span>Gravida</span>
    </div>
  </div>
</aside>

<!-- posts -->
<main>
  <article class="post" style="left:432px;top:810px;width:712px">
    <h2 class="post-title">Nam fermentum vestibulum purus....</h2>
    <div class="share"></div>
    <div class="meta"><span>▪ Mar 16, 2017</span><span>● By Maya</span></div>
    <div class="post-image" role="img" aria-label="Illustration of a figure climbing a rising graph drawn by a hand" style="height:370px;background:linear-gradient(135deg,#eef4f8,#a9cde3)"></div>
    <p class="excerpt">Aliquam molestie, mi id imperdiet euismod, dui purus auctor tellus, et interdum lacus lectus ac ante. Sed accumsan sollicitudin sapien, sit amet adipiscing turpis gravida ac. In congue, neque ac lobortis volutpat, libero mauris cursus mi, vitae suscipit erat tortor non tellus.</p>
    <div class="post-foot"><span class="read-more">READ MORE ›</span><span class="comments">▭ 0 COMMENTS</span></div>
  </article>

  <article class="post" style="left:432px;top:1456px;width:712px">
    <h2 class="post-title">Nam fermentum vestibulum purus....</h2>
    <div class="share"></div>
    <div class="meta"><span>▪ Mar 16, 2017</span><span>● By Maya</span></div>
    <div class="post-image" role="img" aria-label="Photo of a smiling woman raising her arms at her desk" style="height:390px;background:linear-gradient(135deg,#f7f7f5,#cfcac2)"></div>
    <p class="excerpt">Aliquam molestie, mi id imperdiet euismod, dui purus auctor tellus, et interdum lacus lectus ac ante. Sed accumsan sollicitudin sapien, sit amet adipiscing turpis gravida ac. In congue, neque ac lobortis volutpat, libero mauris cursus mi, vitae suscipit erat tortor non tellus.</p>
    <div class="post-foot"><span class="read-more">READ MORE ›</span><span class="comments">▭ 0 COMMENTS</span></div>
  </article>

  <article class="post post-small" style="left:432px;top:2166px;width:344px">
    <h2 class="post-title">Nam fermentum....</h2>
    <div class="share"></div>
    <div class="meta"><span>▪ Mar 16, 2017</span><span>● By Maya</span></div>
    <div class="post-image" role="img" aria-label="Photo of friends with raised hands against a sunset" style="height:230px;background:linear-gradient(180deg,#f6c45a,#e27b22 60%,#3a2514)"></div>
    <p class="excerpt">Aliquam molestie, mi id imperdiet euismod, dui purus auctor tellus, et interdum lacus lectus ac ante.</p>
    <div class="post-foot"><span class="read-more">READ MORE ›</span><span class="comments">▭ 0 COMMENTS</span></div>
  </article>

  <article class="post post-small" style="left:800px;top:2166px;width:344px">
    <h2 class="post-title">Nam fermentum....</h2>
    <div class="share"></div>
    <div class="meta"><span>▪ Mar 16, 2017</span><span>● By Maya</span></div>
    <div class="post-image" role="img" aria-label="Photo of a hand turning a glowing green dial" style="height:230px;background:radial-gradient(circle at 60% 50%,#7fb04a,#2a3a22 60%,#111)"></div>
    <p class="excerpt">Aliquam molestie, mi id imperdiet euismod, dui purus auctor tellus, et interdum lacus lectus ac ante.</p>
    <div class="post-foot"><span class="read-more">READ MORE ›</span><span class="comments">▭ 0 COMMENTS</span></div>
  </article>

  <div class="pagination abs"><span class="arrow">‹</span><span class="active">1</span><span>2</span><span>3</span><span>4</span><span>5</span><span class="arrow">›</span></div>
</main>

<footer class="site-footer abs">Copyright © 2017, Bright Meadow Notes. All Rights Reserved.</footer>

</body>
</html>
```